Falcrest security business card

Looking for a business card for my security company

Target Market(s)

Security

Industry/Entity Type

Security

Contact Information for Business Card

Name - Gil Marston. Title - General manager - direct 314 862.4490 website www. falcrestsecurityservices.example email - gil@ falcrestsecurityservices.example

Requirements
Must have
• Logo attached

```html
<!DOCTYPE html>
<html lang="en">
<head>
<meta charset="utf-8">
<title>Falcrest Security Services – Business Card</title>
<link rel="stylesheet" href="https://fonts.googleapis.com/css2?family=Montserrat:wght@300;400;700;800&display=swap">
<style>
  :root {
    --backdrop: #2a2a2d;
    --card-black: #0d0d0d;
    --card-white: #ffffff;
    --gold: #c9a66b;
    --gold-light: #e8d2a4;
    --gold-dark: #8c6a3a;
    --text-light: #f2f2f2;
    --text-muted: #8a8a8a;
  }
  * { box-sizing: border-box; margin: 0; padding: 0; }
  html, body {
    width: 1200px; height: 947px; overflow: hidden;
    background: var(--backdrop);
    font-family: "Montserrat", sans-serif;
  }
  .canvas { position: relative; width: 1200px; height: 947px; }
  .card {
    position: absolute; width: 640px; height: 370px;
    border-radius: 22px; overflow: hidden;
    box-shadow: 0 20px 40px rgba(0,0,0,.45);
  }
  .card-front {
    left: 60px; top: 60px;
    background: var(--card-black);
    display: flex; align-items: center; justify-content: center;
  }
  .card-back { left: 500px; top: 517px; background: var(--card-white); }
  .card-back .backdrop-shape { position: absolute; inset: 0; width: 100%; height: 100%; }
  .brand-name {
    font-weight: 800; color: var(--gold);
    text-transform: uppercase; letter-spacing: 2px;
    display: flex; align-items: center; gap: 16px;
  }
  .brand-mark { width: 22px; height: 22px; border-radius: 50%; background: var(--gold); }
  .card-front .brand-name { font-size: 70px; }
  .card-back .brand-name {
    position: absolute; left: 36px; top: 40px; font-size: 44px; gap: 12px;
  }
  .card-back .brand-mark { width: 16px; height: 16px; }
  .holder { position: absolute; left: 48px; bottom: 40px; }
  .holder-name {
    font-size: 30px; font-weight: 700; color: var(--gold-light);
    text-transform: uppercase; letter-spacing: 1px;
  }
  .holder-title { font-size: 17px; font-weight: 300; color: var(--text-muted); margin-top: 4px; }
  .contact-list {
    position: absolute; right: 34px; top: 190px; list-style: none;
    display: flex; flex-direction: column; gap: 10px;
  }
  .contact-item {
    display: flex; align-items: center; gap: 12px;
    font-size: 15px; font-weight: 300; color: var(--text-light);
  }
  .contact-icon {
    width: 18px; height: 18px; border-radius: 50%; background: var(--gold);
    display: flex; align-items: center; justify-content: center; flex: none;
  }
  .contact-icon svg { width: 10px; height: 10px; }
</style>
</head>
<body>
<main class="canvas">

  <section class="card card-front" aria-label="Card front">
    <div class="brand-name"><span class="brand-mark"></span>Falcrest</div>
  </section>

  <section class="card card-back" aria-label="Card back">
    <svg class="backdrop-shape" viewBox="0 0 640 370" preserveAspectRatio="none" aria-hidden="true">
      <defs>
        <linearGradient id="swoosh-gold" x1="0" y1="1" x2="1" y2="0">
          <stop offset="0" stop-color="#e8d2a4"/>
          <stop offset=".5" stop-color="#c9a66b"/>
          <stop offset="1" stop-color="#8c6a3a" stop-opacity=".3"/>
        </linearGradient>
      </defs>
      <path d="M0 250 C100 190 300 140 640 100 L640 90 C300 124 100 172 0 232 Z" fill="url(#swoosh-gold)"/>
      <path d="M0 250 C100 190 300 140 640 100 L640 370 L0 370 Z" fill="#0d0d0d"/>
    </svg>

    <div class="brand-name"><span class="brand-mark"></span>Falcrest</div>

    <div class="holder">
      <p class="holder-name">Gil Marston</p>
      <p class="holder-title">General manager</p>
    </div>

    <ul class="contact-list">
      <li class="contact-item">
        <span class="contact-icon"><svg viewBox="0 0 10 10"><path d="M2 1 L4 3 L3 4 Q4 6 6 7 L7 6 L9 8 L8 9 Q3 9 1 2 Z" fill="#0d0d0d"/></svg></span>
        314 862.4490
      </li>
      <li class="contact-item">
        <span class="contact-icon"><svg viewBox="0 0 10 10"><circle cx="5" cy="5" r="3.6" fill="none" stroke="#0d0d0d" stroke-width="1.2"/><path d="M1.4 5 H8.6 M5 1.4 V8.6" stroke="#0d0d0d" stroke-width="1"/></svg></span>
        www.falcrestsecurityservices.example
      </li>
      <li class="contact-item">
        <span class="contact-icon"><svg viewBox="0 0 10 10"><rect x="1.5" y="2.5" width="7" height="5" fill="none" stroke="#0d0d0d" stroke-width="1.1"/><path d="M1.5 2.5 L5 5.5 L8.5 2.5" fill="none" stroke="#0d0d0d" stroke-width="1.1"/></svg></span>
        gil@falcrestsecurityservices.example
      </li>
    </ul>
  </section>

</main>
</body>
</html>
```